Home Page Redesign for Pet Website

Looking to redesign the home page of our WORDPRESS website which will be renamed The Critter Cover Handbook 2015.

Looking for clean design which communicates clarity.
Updates

This is for a Wordpress site.

Please note that the design MUST include the content which is shown in the table in the brief!

Hi Thanks for the designs so far. We have just updated the brief to provide more information and clarify a few issues. We have also now included a couple of layout suggestions. They are just suggestions but it should give you a better idea of what we are looking for. And we have just increased the budget for 1st place by £120. Please feel free to message me if you have any questions. Many thanks. Maud

Please note that the new brief is in a file dated 25 Jan!

Reason: We have extended the deadline so we can continue working with the designers who have submitted designs we like. If you have any new designs please submit them by the original deadline of 7.37pm this evening (GMT). We are planning to make our final decision by Friday this week.

Target Market(s)

UK pet owners. All ages but largest age group is 35-50.

Industry/Entity Type

Insurance

Requirements
Must have
• Three clear content groups - LEARN, RESEARCH, CAMPAIGN (see brief for more details).
Stock photos with dogs and cats
Use current colour scheme
Must work with existing inner pages.
Existing font.. but 1pt larger
See brief for more details
Should not have
• Logo
Content from Existing Page (except for footer content... and menu headings).

```html
<!DOCTYPE html>
<html lang="en">
<head>
<meta charset="utf-8">
<title>The Critter Cover Handbook 2015</title>
<link href="https://fonts.googleapis.com/css2?family=Open+Sans:wght@400;600;700&family=Noto+Serif:wght@400&display=swap" rel="stylesheet">
<style>
:root{
  --nav:#3a3a3a;
  --accent:#e8663a;
  --hero-a:#c8562a;
  --hero-b:#f0a070;
  --blue:#2a8fd6;
  --orange:#f39223;
  --purple:#9b55c8;
  --green:#5fae5a;
  --grey:#7a7a7a;
  --light:#f1f1f1;
  --page:#ececec;
  --dark:#3b3b3b;
  --darker:#2e2e2e;
  --white:#fff;
  --text:#555;
}
*{box-sizing:border-box;margin:0;padding:0}
html,body{width:789px;height:1200px;overflow:hidden}
body{background:var(--page);font-family:"Open Sans",sans-serif;color:var(--text);position:relative}
.nav{height:36px;background:var(--nav);display:flex;align-items:center;padding:0 14px;gap:14px}
.nav a{color:#eee;font-size:9px;font-weight:600;text-decoration:none;letter-spacing:.3px}
.nav .search{margin-left:auto;background:var(--accent);color:#fff;font-size:8px;padding:5px 8px;width:130px;border-radius:2px;display:flex;justify-content:space-between}
.hero{height:344px;position:relative;background:linear-gradient(100deg,var(--hero-a) 0%,#d8723e 45%,var(--hero-b) 100%)}
.hero .photo{position:absolute;right:0;top:0;width:470px;height:100%;background:radial-gradient(ellipse at 60% 55%,#f3c79a 0%,#e08850 55%,transparent 80%)}
.hero-text{position:absolute;left:86px;top:70px;color:#fff}
.hero h1{font-family:"Noto Serif",serif;font-weight:400;font-size:34px;line-height:1.1}
.hero p{font-size:15px;margin-top:14px;line-height:1.35;width:270px}
.hero .btn{display:inline-block;margin-top:22px;border:1.5px solid #fff;color:#fff;font-size:9px;font-weight:700;padding:7px 12px;letter-spacing:.5px}
.dots{position:absolute;left:50%;bottom:14px;display:flex;gap:6px;transform:translateX(-50%)}
.dots span{width:6px;height:6px;border-radius:50%;background:rgba(255,255,255,.55)}
.dots span:first-child{background:#fff}
.wrap{width:616px;margin:0 auto}
.groups{display:flex;margin-top:34px;height:160px}
.group{flex:1;padding:12px 12px;color:#fff}
.group.learn{background:var(--blue)}
.group.research{background:var(--orange)}
.group.campaign{background:var(--purple)}
.group h2{font-size:9px;font-weight:700;text-align:center;margin-bottom:8px;white-space:nowrap}
.group ul{list-style:none}
.group li{font-size:6.5px;font-weight:600;line-height:1.3;margin-bottom:2.5px;padding-left:9px;position:relative}
.group li::before{content:"";position:absolute;left:0;top:2.5px;width:3.5px;height:3.5px;background:#fff}
.info{display:flex;margin-top:18px;height:270px}
.info>div{flex:1;padding:12px 12px}
.popular{background:var(--green);color:#fff}
.bio{background:var(--grey);color:#fff}
.disclaimer{background:var(--light)}
.info h3{font-size:10px;font-weight:700;margin-bottom:10px;padding-bottom:6px;border-bottom:1px solid rgba(255,255,255,.4)}
.disclaimer h3{border-color:#ccc;color:#666}
.popular .item{font-size:7px;line-height:1.4;margin-bottom:12px}
.popular .date{display:block;opacity:.8}
.bio .pic{height:120px;background:linear-gradient(135deg,#5a4a3a,#a08868);margin-bottom:8px}
.bio p,.disclaimer p{font-size:7px;line-height:1.5}
.social{position:absolute;left:0;top:900px;width:100%;height:152px;background:var(--dark)}
.social .wrap{display:flex;justify-content:space-between;padding-top:12px}
.col{width:150px;text-align:center;color:#fff}
.col h4{font-size:12px;font-weight:600;letter-spacing:.3px;margin-bottom:10px;white-space:nowrap}
.box{height:104px;background:#fff}
.ad{display:flex;align-items:center;justify-content:center;color:#444;font-size:22px;font-weight:700;line-height:1.05}
.feed{padding:6px;text-align:left}
.feed .head{display:flex;gap:5px;align-items:center;font-size:6px;color:#335;font-weight:600}
.feed .head i{width:16px;height:16px;background:#9ab;display:block}
.feed .grid{margin-top:6px;height:68px;background:linear-gradient(90deg,#d8dde6,#c4ccd8)}
.footer-links{position:absolute;top:1052px;left:0;width:100%;height:53px;background:var(--darker);text-align:center;padding-top:9px}
.footer-links nav{display:flex;justify-content:center;gap:14px}
.footer-links a{color:#ddd;font-size:7px;text-decoration:none;font-weight:600}
.icons{display:flex;justify-content:center;gap:6px;margin-top:8px}
.icons span{width:14px;height:14px;border-radius:50%;background:#8a8a8a}
.legal{position:absolute;top:1105px;left:0;width:100%;height:95px;background:#e4e4e4;text-align:center;font-size:6.5px;color:#888;padding-top:30px;line-height:1.6}
</style>
</head>
<body>
<header class="nav">
  <a>HOME</a><a>PET INSURANCE REVIEWS</a><a>PROVIDER A-Z</a><a>PET INSURANCE POLICIES</a><a>SURVEYS</a><a>N. MORE</a>
  <div class="search"><span>Search here</span><span>&#9906;</span></div>
</header>

<section class="hero">
  <div class="photo" role="img" aria-label="Photo of a cat and a small dog sitting together"></div>
  <div class="hero-text">
    <h1>The Critter Cover<br>Handbook 2015</h1>
    <p>Independent unbiased information for fellow pet owners</p>
    <span class="btn">LEARN MORE</span>
  </div>
  <div class="dots"><span></span><span></span><span></span></div>
</section>

<main class="wrap">
  <section class="groups">
    <div class="group learn">
      <h2>Learn About Pet Insurance</h2>
      <ul>
        <li>Introduction to Pet Insurance</li>
        <li>Pet Cover Types</li>
        <li>What to Consider Before Buying</li>
        <li>Ten Popular Pet Insurance Providers</li>
        <li>Confused by Pet Insurance? Start Here</li>
        <li>Third Party Liability Insurance</li>
        <li>Do Not Assume Insurers Will Pay</li>
        <li>Why Cheap Pet Insurance is Risky</li>
        <li>Why Your Vet History Matters</li>
      </ul>
    </div>
    <div class="group research">
      <h2>Research Pet Insurance Policies</h2>
      <ul>
        <li>Analysis, Customer Reviews and Full Details of All UK Policies</li>
        <li>Comparison</li>
        <li>Policies</li>
        <li>Prices</li>
        <li>Search our database for policies matching your criteria</li>
        <li>Compare claim experiences, by pet insurance providers</li>
      </ul>
    </div>
    <div class="group campaign">
      <h2>Campaign For Fairer Pet Insurance</h2>
      <ul>
        <li>Analysis, Customer Reviews and Full Details of All UK Policies</li>
        <li>Milestones</li>
        <li>Progress</li>
        <li>Reports</li>
        <li>Search our database for policies matching your criteria</li>
        <li>Compare claim experiences, by pet insurance providers</li>
      </ul>
    </div>
  </section>

  <section class="info">
    <div class="popular">
      <h3>Popular Resources</h3>
      <p class="item">Unique reader review and helpful comments for better decisions<span class="date">17.05.2015</span></p>
      <p class="item">Unique reader review and helpful comments for better decisions<span class="date">17.05.2015</span></p>
      <p class="item">Unique reader review and helpful comments for better decisions<span class="date">17.05.2015</span></p>
    </div>
    <div class="bio">
      <h3>Bio</h3>
      <div class="pic" role="img" aria-label="Photo of a dog lying on grass"></div>
      <p>Maud loves her cats and dogs and started this guide to help fellow owners choose fair cover.</p>
    </div>
    <div class="disclaimer">
      <h3>Disclaimer</h3>
      <p>Please note that pet insurance terms often change. While we try our best to keep this site up to date, always check details with the provider before buying. If you find any mistakes on this site please let us know so we can correct them for the benefit of future visitors. Many thanks!</p>
    </div>
  </section>
</main>

<section class="social">
  <div class="wrap">
    <div class="col">
      <h4>ADD HERE</h4>
      <div class="box ad">AD<br>HERE</div>
    </div>
    <div class="col">
      <h4>JOIN US ON PAWBOOK</h4>
      <div class="box feed">
        <div class="head"><i></i>Critter Cover Polls</div>
        <div class="grid" role="img" aria-label="Grid of follower profile photos"></div>
      </div>
    </div>
    <div class="col">
      <h4>LATEST FROM CHIRPER</h4>
      <div class="box feed">
        <div class="head"><i></i>Critter Cover Polls</div>
        <div class="grid" role="img" aria-label="Grid of follower profile photos"></div>
      </div>
    </div>
  </div>
</section>

<footer>
  <div class="footer-links">
    <nav><a>ABOUT US</a><a>LEGAL INFORMATION &amp; DISCLAIMERS</a><a>PRIVACY POLICY</a></nav>
    <div class="icons"><span></span><span></span><span></span></div>
  </div>
  <div class="legal">
    About Us | Legal Information &amp; Disclaimers | Privacy Policy<br>
    copyright © 2015 The Critter Cover Handbook. All Rights Reserved
  </div>
</footer>
</body>
</html>
```